Brisa Pastry Mill Business card

We are empanada whole-sellers and I want a business card design with a picture of an empanada on it that also mentions first trial order FREE. our contact number 555-214-7093 our website www.brisapastry.example and business email Tobin@brisapastry.example

If you want any of our artwork please feel free to email me at the address above.

```html
<!DOCTYPE html>
<html lang="en">
<head>
<meta charset="utf-8">
<title>Brisa Pastry Mill Business Card</title>
<link rel="stylesheet" href="https://fonts.googleapis.com/css2?family=Open+Sans:wght@400;600&family=Dancing+Script:wght@600&display=swap">
<style>
  :root {
    --stage: #3b3b3b;
    --card-blue: #5b97d3;
    --sky: #2aa8e0;
    --wave-blue: #4f8dcc;
    --wave-grey: #4a4a4a;
    --ink: #1d1d1d;
    --paper: #ffffff;
    --crust-light: #e3b46a;
    --crust-dark: #b87a33;
    --logo-cream: #eed9a8;
  }
  * { margin: 0; padding: 0; box-sizing: border-box; }
  html, body { width: 1200px; height: 750px; overflow: hidden; }
  body { background: var(--stage); font-family: "Open Sans", sans-serif; position: relative; }

  .card {
    position: absolute; top: 210px; width: 511px; height: 293px;
    border-radius: 22px; overflow: hidden;
  }
  .card--front { left: 78px; background: var(--card-blue); }
  .card--back { left: 608px; background: var(--paper); }

  .food-photo {
    position: absolute; right: 0; top: 0; width: 220px; height: 100%;
    background: radial-gradient(ellipse at 55% 60%, var(--crust-light) 0%, var(--crust-dark) 45%, #d9d6cf 80%);
    -webkit-mask-image: linear-gradient(to right, transparent 0, #000 70px);
    mask-image: linear-gradient(to right, transparent 0, #000 70px);
  }

  .brand-mark { position: absolute; display: flex; align-items: center; gap: 10px; }
  .brand-mark__dot { width: 46px; height: 46px; border-radius: 50%; background: var(--sky); flex: none; }
  .brand-mark__name { font-weight: 600; font-size: 24px; line-height: 1.1; }
  .card--front .brand-mark { left: 34px; top: 105px; }
  .card--front .brand-mark__name { color: var(--ink); }
  .card--front .brand-mark__dot { background: var(--logo-cream); }
  .card--back .brand-mark { left: 24px; top: 70px; }
  .card--back .brand-mark__name { color: var(--ink); font-size: 22px; }

  .offer {
    position: absolute; left: 28px; top: 238px;
    font-family: "Dancing Script", cursive; font-weight: 600;
    font-size: 31px; color: var(--ink); white-space: nowrap;
  }

  .contact { position: absolute; right: 30px; top: 126px; text-align: right; color: var(--ink); }
  .contact__name { color: var(--sky); font-size: 15px; letter-spacing: 0.5px; line-height: 19px; }
  .contact__title { font-size: 15px; line-height: 19px; margin-bottom: 13px; }
  .contact__line { font-size: 15px; line-height: 19.5px; display: flex; justify-content: flex-end; align-items: center; gap: 6px; }
  .contact__line svg { width: 12px; height: 12px; flex: none; }

  .waves { position: absolute; left: 0; bottom: 0; width: 511px; height: 70px; }
</style>
</head>
<body>

<section class="card card--front">
  <div class="food-photo" role="img" aria-label="Photo of golden fried empanadas in a basket with a green dipping sauce"></div>
  <div class="brand-mark">
    <span class="brand-mark__dot"></span>
    <span class="brand-mark__name">Brisa Pastry Mill</span>
  </div>
  <p class="offer">first trial order FREE</p>
</section>

<section class="card card--back">
  <div class="brand-mark">
    <span class="brand-mark__dot"></span>
    <span class="brand-mark__name">Brisa Pastry Mill</span>
  </div>

  <div class="contact">
    <p class="contact__name">YOUR NAME PLS</p>
    <p class="contact__title">title here</p>
    <p class="contact__line">555-214-7093
      <svg viewBox="0 0 12 12"><path fill="#2aa8e0" d="M1 5c0-2 2-3 5-3s5 1 5 3l-2 .5-.5-1.5h-5L3 5.5zM3 6h6l1 4H2z"/></svg>
    </p>
    <p class="contact__line">www.brisapastry.example
      <svg viewBox="0 0 12 12" fill="none" stroke="#2aa8e0" stroke-width="1"><circle cx="6" cy="6" r="5"/><ellipse cx="6" cy="6" rx="2.2" ry="5"/><path d="M1 6h10M2 3.5h8M2 8.5h8"/></svg>
    </p>
    <p class="contact__line">Tobin@brisapastry.example
      <svg viewBox="0 0 12 12"><rect x="0.5" y="2.5" width="11" height="7.5" fill="#2aa8e0"/><path d="M0.5 2.5 6 7l5.5-4.5" fill="none" stroke="#fff" stroke-width="1"/></svg>
    </p>
  </div>

  <svg class="waves" viewBox="0 0 511 70" preserveAspectRatio="none">
    <path d="M0 16 C120 0 260 40 380 30 C440 25 490 14 511 4 L511 10 C480 24 430 32 380 36 C260 46 120 8 0 22Z" fill="var(--wave-grey)"/>
    <path d="M0 22 C120 8 260 46 380 36 C440 32 490 22 511 14 L511 70 L0 70Z" fill="var(--sky)"/>
    <path d="M0 34 C120 20 260 54 380 44 C440 40 490 32 511 26 L511 70 L0 70Z" fill="#ffffff"/>
    <path d="M0 37 C120 23 260 57 380 47 C440 43 490 35 511 29 L511 70 L0 70Z" fill="var(--wave-blue)"/>
  </svg>
</section>

</body>
</html>
```